Recreate a graphic of The Church Year

Take the uploaded graphic and recreate it (without the shield) for use by PWD, branding it with the PDW logo.

Target Market(s)

For use by PDW

Industry/Entity Type

Education

Font styles to use
Sans Serif

Requirements
Must have
• Use liturgical colors as in upload.
• The center of the circle must be empty except for the words The Church Year
• The PDW logo must be on the graphic
Nice to have
• None.

```html
<!DOCTYPE html>
<html lang="en">
<head>
<meta charset="utf-8">
<title>The Seasons of the Church Year — PDW</title>
<link rel="stylesheet" href="https://fonts.googleapis.com/css2?family=Lato:wght@700;900&display=swap">
<style>
  :root {
    --sky: #d9f1fc;
    --centre-light: #e4f6fd;
    --centre-edge: #b9d6e4;
    --ink: #0b0b0b;
    --brand-blue: #1a6fb0;
    --lent: #6a10d2;
    --lent-deep: #3c3592;
    --easter: #d89c00;
    --easter-deep: #8a5600;
    --passion-red: #c8102e;
    --passion-black: #121212;
    --ordinary: #0a9e3c;
    --ordinary-light: #22c86d;
    --creation: #f15a24;
    --creation-light: #f7983a;
    --advent: #5b16c9;
    --christmas: #f6f6f6;
    --christmas-gold: #e0a100;
    --white: #ffffff;
  }
  * { margin: 0; padding: 0; box-sizing: border-box; }
  html, body { width: 1200px; height: 910px; overflow: hidden; background: var(--sky); }
  .poster {
    position: relative; width: 1200px; height: 910px; background: var(--sky);
    font-family: "Lato", Arial, sans-serif;
  }
  .brand {
    position: absolute; left: 100px; top: 92px;
    font-weight: 900; font-size: 84px; line-height: 1; letter-spacing: 2px;
    color: var(--brand-blue);
  }
  .wheel { position: absolute; left: 0; top: 0; }
  .wheel text { font-family: "Lato", Arial, sans-serif; }
  .title { font-weight: 900; font-size: 53px; fill: var(--ink); }
  .callout-text { font-weight: 900; font-size: 25px; fill: var(--white); }
  .ring-text { font-weight: 900; font-size: 22px; fill: var(--white); }
  .ring-text--gold { fill: var(--christmas-gold); }
  .marker { font-weight: 900; font-size: 14px; fill: var(--ink); }
  .leader { fill: none; stroke: var(--ink); stroke-width: 1; }
</style>
</head>
<body>
<div class="poster">
  <div class="brand">PDW</div>

  <svg class="wheel" width="1200" height="910" viewBox="0 0 1200 910">
    <defs>
      <radialGradient id="centreFill" cx="600" cy="458" r="244" gradientUnits="userSpaceOnUse">
        <stop offset="0.8" stop-color="var(--centre-light)"/>
        <stop offset="1" stop-color="var(--centre-edge)"/>
      </radialGradient>
      <linearGradient id="lentGrad" x1="0" y1="190" x2="0" y2="560" gradientUnits="userSpaceOnUse">
        <stop offset="0" stop-color="var(--lent)"/>
        <stop offset="1" stop-color="var(--lent-deep)"/>
      </linearGradient>
      <linearGradient id="easterGrad" x1="470" y1="0" x2="800" y2="0" gradientUnits="userSpaceOnUse">
        <stop offset="0" stop-color="var(--easter-deep)"/>
        <stop offset="0.7" stop-color="var(--easter)"/>
      </linearGradient>
      <linearGradient id="creationGrad" x1="830" y1="0" x2="910" y2="0" gradientUnits="userSpaceOnUse">
        <stop offset="0" stop-color="var(--creation-light)"/>
        <stop offset="1" stop-color="var(--creation)"/>
      </linearGradient>
      <linearGradient id="adventGrad" x1="550" y1="0" x2="760" y2="0" gradientUnits="userSpaceOnUse">
        <stop offset="0" stop-color="var(--lent-deep)"/>
        <stop offset="1" stop-color="var(--advent)"/>
      </linearGradient>
      <linearGradient id="adventTag" x1="528" y1="0" x2="728" y2="0" gradientUnits="userSpaceOnUse">
        <stop offset="0" stop-color="var(--lent)"/>
        <stop offset="1" stop-color="var(--lent-deep)"/>
      </linearGradient>
      <path id="arcClockwise" d="M327 458 A273 273 0 1 1 873 458 A273 273 0 1 1 327 458"/>
      <path id="arcCounter" d="M600 164 A294 294 0 1 0 600 752 A294 294 0 1 0 600 164"/>
    </defs>

    <!-- centre -->
    <circle cx="600" cy="458" r="244" fill="url(#centreFill)"/>

    <!-- seasons ring -->
    <g class="ring">
      <path d="M294.0 551.6 A320 320 0 0 1 421.1 192.7 L463.6 255.7 A244 244 0 0 0 366.7 529.3 Z" fill="url(#lentGrad)"/>
      <path d="M421.1 192.7 A320 320 0 0 1 440 180.9 L478 246.7 A244 244 0 0 0 463.6 255.7 Z" fill="var(--passion-red)"/>
      <path d="M440 180.9 A320 320 0 0 1 475.0 163.4 L504.7 233.4 A244 244 0 0 0 478 246.7 Z" fill="var(--passion-black)"/>
      <path d="M475.0 163.4 A320 320 0 0 1 792.6 202.4 L746.8 263.1 A244 244 0 0 0 504.7 233.4 Z" fill="url(#easterGrad)"/>
      <path d="M792.6 202.4 A320 320 0 0 1 805.7 212.9 L756.8 271.1 A244 244 0 0 0 746.8 263.1 Z" fill="var(--passion-red)"/>
      <path d="M805.7 212.9 A320 320 0 0 1 818.2 224.0 L766.4 279.5 A244 244 0 0 0 756.8 271.1 Z" fill="var(--easter)"/>
      <path d="M818.2 224.0 A320 320 0 0 1 910.5 380.6 L836.8 399.0 A244 244 0 0 0 766.4 279.5 Z" fill="var(--ordinary)"/>
      <path d="M910.5 380.6 A320 320 0 0 1 906.0 551.6 L833.3 529.3 A244 244 0 0 0 836.8 399.0 Z" fill="url(#creationGrad)"/>
      <path d="M906.0 551.6 A320 320 0 0 1 760 735.1 L722 669.3 A244 244 0 0 0 833.3 529.3 Z" fill="var(--ordinary)"/>
      <path d="M760 735.1 A320 320 0 0 1 544.4 773.1 L557.6 698.3 A244 244 0 0 0 722 669.3 Z" fill="url(#adventGrad)"/>
      <path d="M544.4 773.1 A320 320 0 0 1 407.4 713.6 L453.2 652.9 A244 244 0 0 0 557.6 698.3 Z" fill="var(--christmas)"/>
      <path d="M407.4 713.6 A320 320 0 0 1 294.0 551.6 L366.7 529.3 A244 244 0 0 0 453.2 652.9 Z" fill="var(--ordinary)"/>
      <circle cx="600" cy="458" r="256" fill="none" stroke="var(--white)" stroke-opacity="0.16" stroke-width="24"/>
      <circle cx="600" cy="458" r="314" fill="none" stroke="#000" stroke-opacity="0.06" stroke-width="12"/>
    </g>

    <!-- ring labels -->
    <text class="ring-text"><textPath href="#arcClockwise" startOffset="26.7%" text-anchor="middle">50 Days</textPath></text>
    <text class="ring-text"><textPath href="#arcClockwise" startOffset="50.4%" text-anchor="middle">5 Sundays</textPath></text>
    <text class="ring-text"><textPath href="#arcCounter" startOffset="52.6%" text-anchor="middle">4 Sundays</textPath></text>
    <text class="ring-text ring-text--gold"><textPath href="#arcCounter" startOffset="43.4%" text-anchor="middle">12 Days</textPath></text>
    <text class="ring-text"><textPath href="#arcCounter" startOffset="34.6%" text-anchor="middle">4-8 Sundays</textPath></text>

    <!-- title -->
    <text class="title" x="595" y="426" text-anchor="middle">The Seasons</text>
    <text class="title" x="595" y="480" text-anchor="middle">of the Church Year</text>

    <!-- season callouts -->
    <g class="callout">
      <path d="M546 100 L534 138 L572 118 Z" fill="var(--easter)"/>
      <rect x="546" y="72" width="192" height="46" rx="7" fill="var(--easter)"/>
      <text class="callout-text" x="642" y="104" text-anchor="middle">Easter Season</text>
    </g>
    <g class="callout">
      <path d="M262 300 L294 328 L280 290 Z" fill="var(--lent)"/>
      <rect x="83" y="262" width="197" height="47" rx="7" fill="var(--lent)"/>
      <text class="callout-text" x="181" y="294" text-anchor="middle">Season of Lent</text>
    </g>
    <g class="callout">
      <path d="M946 450 L932 482 L972 461 Z" fill="var(--creation)"/>
      <rect x="946" y="414" width="192" height="47" rx="7" fill="var(--creation)"/>
      <text class="callout-text" x="1042" y="446" text-anchor="middle">Creation Time</text>
    </g>
    <g class="callout">
      <path d="M900 668 L878 690 L924 680 Z" fill="var(--ordinary)"/>
      <rect x="894" y="610" width="170" height="70" rx="7" fill="var(--ordinary)"/>
      <text class="callout-text" x="979" y="642" text-anchor="middle">Season after</text>
      <text class="callout-text" x="979" y="666" text-anchor="middle">Pentecost</text>
    </g>
    <g class="callout">
      <path d="M288 628 L316 650 L302 616 Z" fill="var(--ordinary)"/>
      <rect x="84" y="586" width="218" height="46" rx="7" fill="var(--ordinary)"/>
      <text class="callout-text" x="193" y="617" text-anchor="middle">Epiphany Season</text>
    </g>
    <g class="callout">
      <path d="M470 810 L501 786 L486 824 Z" fill="var(--easter)"/>
      <rect x="268" y="805" width="218" height="46" rx="7" fill="var(--easter)"/>
      <text class="callout-text" x="377" y="836" text-anchor="middle">Christmas Season</text>
    </g>
    <g class="callout">
      <path d="M712 810 L741 786 L728 824 Z" fill="var(--lent-deep)"/>
      <rect x="528" y="805" width="200" height="46" rx="7" fill="url(#adventTag)"/>
      <text class="callout-text" x="628" y="836" text-anchor="middle">Advent Season</text>
    </g>

    <!-- day markers -->
    <g class="markers">
      <text class="marker" x="456" y="115" text-anchor="end">Easter Sunday</text>
      <polyline class="leader" points="460,110 474,110 502,160"/>
      <text class="marker" x="438" y="133" text-anchor="end">Holy Saturday</text>
      <polyline class="leader" points="440,128 453,128 478,178"/>
      <text class="marker" x="417" y="152" text-anchor="end">Good Friday</text>
      <polyline class="leader" points="420,147 435,147 453,186"/>
      <text class="marker" x="400" y="172" text-anchor="end">Palm Sunday</text>
      <polyline class="leader" points="404,167 418,167 438,202"/>

      <text class="marker" x="830" y="199">Pentecost</text>
      <polyline class="leader" points="826,194 816,194 798,214"/>
      <text class="marker" x="840" y="213">Trinity</text>
      <polyline class="leader" points="836,208 824,208 808,232"/>

      <text class="marker" x="944" y="371">September 1st</text>
      <text class="marker" x="945" y="386">Creation Time</text>
      <polyline class="leader" points="936,368 928,368 906,392"/>

      <text class="marker" x="990" y="530" text-anchor="middle">October 4th</text>
      <text class="marker" x="990" y="545" text-anchor="middle">St. Francis of Assisi</text>
      <polyline class="leader" points="934,526 924,526 902,550"/>

      <text class="marker" x="778" y="755">Christ the King Sunday</text>
      <polyline class="leader" points="776,750 764,750 744,726"/>

      <text class="marker" x="266" y="542" text-anchor="end">Ash Wednesday</text>
      <polyline class="leader" points="270,537 284,537 304,552"/>

      <text class="marker" x="380" y="715" text-anchor="end">Epiphany</text>
      <polyline class="leader" points="384,710 394,710 405,694"/>
      <text class="marker" x="384" y="746" text-anchor="end">Feast of the Holy Innocents</text>
      <polyline class="leader" points="386,741 408,741 432,696"/>
      <text class="marker" x="406" y="767" text-anchor="end">St. Stephen the Martyr</text>
      <polyline class="leader" points="408,762 430,762 454,718"/>
      <text class="marker" x="422" y="786" text-anchor="end">Christmas Day</text>
      <polyline class="leader" points="428,781 448,781 474,736"/>
    </g>
  </svg>
</div>
</body>
</html>
```